metal roofing website

I have several domain names and a website that has been built. I need someone to recreate essentially the same website and change some photos and basic design to create the new sites. I have all of the files and c panel access to the lucky winner. If you can do a good job at a fair price I will have 100's of sites to send to you very soon. I have the site built and have all files just need it recreated on my server. the current site is www.dorvanemetalinc.com I am looking to get this done ASAP!!!

```html
<!DOCTYPE html>
<html lang="en">
<head>
<meta charset="utf-8">
<title>Dorvane Metal Inc. – Post Frame Buildings &amp; Metal Roofing</title>
<link href="https://fonts.googleapis.com/css2?family=Raleway:wght@500;600;700;800&family=Open+Sans:wght@400;600;700&display=swap" rel="stylesheet">
<style>
:root{
  --red:#b5281f;
  --red-dark:#9f2119;
  --beige:#e4d8c8;
  --cream:#f8f4ee;
  --nav:#2a2a2a;
  --charcoal:#3a3a3a;
  --stat-bg:#45484a;
  --ink:#222222;
  --muted:#6f6f6f;
  --white:#ffffff;
  --gold:#f4c21b;
}
*{box-sizing:border-box;margin:0;padding:0}
html,body{width:1200px;height:2616px;overflow:hidden}
body{font-family:"Open Sans",Arial,sans-serif;color:var(--ink);background:var(--white);position:relative}
section,header,footer,nav{position:absolute;left:0;width:1200px}
.abs{position:absolute}
.heading{font-family:"Raleway",Arial,sans-serif;font-weight:700;text-transform:uppercase}
.btn{position:absolute;background:var(--red);color:var(--white);font-family:"Raleway",Arial,sans-serif;font-weight:700;font-size:10px;text-transform:uppercase;display:flex;align-items:center;justify-content:center;letter-spacing:.3px}
.rule{position:absolute;height:3px;width:36px;background:var(--red)}

/* top bar */
.topbar{top:0;height:87px;background:var(--beige)}
.brand{left:227px;top:24px;display:flex;align-items:center;gap:10px}
.brand-mark{width:26px;height:26px;background:var(--red)}
.brand-name{font-family:"Raleway",Arial,sans-serif;font-weight:800;font-size:20px;color:var(--red);letter-spacing:.5px}
.visualizer{left:677px;top:31px;width:106px;height:30px;border:1.5px solid var(--red);color:var(--red);font-family:"Raleway",Arial,sans-serif;font-weight:700;font-size:10px;display:flex;align-items:center;justify-content:center}
.call{left:818px;top:23px;display:flex;align-items:center;gap:10px}
.call small{display:block;font-size:8px;font-weight:700;color:var(--ink);text-transform:uppercase}
.call strong{font-family:"Raleway",Arial,sans-serif;font-size:17px;font-weight:800;color:var(--ink)}

/* nav */
.mainnav{top:87px;height:37px;background:var(--nav)}
.mainnav ul{list-style:none;position:absolute;left:234px;top:0;height:37px;display:flex;gap:0}
.mainnav li{font-family:"Raleway",Arial,sans-serif;font-weight:700;font-size:10px;color:var(--white);line-height:37px;text-transform:uppercase;margin-right:32px;position:relative}
.mainnav li.active:after{content:"";position:absolute;left:0;right:0;bottom:6px;height:2px;background:var(--red)}
.mainnav .btn{left:841px;top:0;height:37px;width:124px}

/* hero */
.hero{top:124px;height:370px}
.hero-photo{position:absolute;inset:0;background:linear-gradient(180deg,#6c7175 0%,#80858a 45%,#5a5e58 78%,#4c5a3a 100%)}
.hero-title{left:234px;top:142px;font-size:25px;line-height:33px;color:var(--white);font-weight:700}
.hero .btn{left:234px;top:218px;width:106px;height:30px}

/* quality strip */
.quality{top:494px;height:87px;background:var(--cream)}
.quality h2{left:234px;top:34px;font-size:15px;color:var(--ink)}
.quality .btn{left:859px;top:28px;width:107px;height:31px}

/* services */
.services{top:581px;height:457px;background:var(--beige)}
.section-title{left:0;width:1200px;text-align:center;font-size:16px;color:var(--ink)}
.services .section-title{top:45px}
.services .rule{left:582px;top:71px}
.card{position:absolute;top:104px;width:232px;height:269px;background:var(--white);box-shadow:0 2px 6px rgba(0,0,0,.12);text-align:center}
.card-photo{height:160px}
.card h3{font-family:"Raleway",Arial,sans-serif;font-weight:700;font-size:11px;line-height:14px;margin-top:22px;text-transform:uppercase;color:var(--ink)}
.card p{font-size:10.5px;line-height:15px;color:var(--muted);margin:3px 20px 0}
.services .btn{left:558px;top:394px;width:106px;height:30px;border-radius:15px}

/* why + stats */
.why{top:1038px;height:376px}
.why-panel{left:0;top:0;width:600px;height:376px;background:var(--red)}
.stats-panel{left:600px;top:0;width:600px;height:376px;background:linear-gradient(180deg,#4d5053 0%,#3e4143 60%,#4a4a44 100%)}
.why h2{top:44px;font-size:16px;color:var(--white)}
.why .rule{background:var(--white);top:70px}
.acc-item{position:absolute;left:234px;width:322px;background:var(--cream);font-family:"Raleway",Arial,sans-serif;font-weight:700;font-size:10px;color:var(--ink)}
.acc-item .acc-head{height:28px;padding:0 12px;display:flex;align-items:center;justify-content:space-between}
.acc-item p{font-family:"Open Sans",Arial,sans-serif;font-weight:400;font-size:8.5px;line-height:12px;color:var(--muted);padding:8px 12px 0;border-top:1px solid #ddd;margin:0 0}
.stat{position:absolute;width:155px;height:75px;border:1.5px solid var(--white);padding:20px 0 0 52px;color:var(--white)}
.stat b{display:block;font-family:"Raleway",Arial,sans-serif;font-weight:800;font-size:16px;color:var(--gold);line-height:18px}
.stat span{font-size:9px;font-weight:600}
.why .btn{left:644px;top:291px;width:95px;height:28px}

/* testimonials */
.clients{top:1414px;height:316px;background:var(--charcoal)}
.clients h2{left:234px;top:50px;font-size:16px;color:var(--white)}
.clients .rule{left:234px;top:76px}
.quote{position:absolute;top:103px;width:222px;color:var(--white)}
.quote p{font-size:9.5px;line-height:14.5px;color:#e9e9e9}
.author{display:flex;align-items:center;gap:12px;margin-top:20px}
.avatar{width:36px;height:36px;background:linear-gradient(135deg,#c9a88c,#8a6a55)}
.author b{display:block;font-family:"Raleway",Arial,sans-serif;font-weight:700;font-size:10px;text-transform:uppercase}
.author small{font-size:8px;color:#dcdcdc}
.dots{left:234px;top:250px;display:flex;gap:8px}
.dots i{width:5px;height:5px;border-radius:50%;background:#888;display:block}
.dots i:first-child{background:var(--red)}

/* projects */
.projects{top:1730px;height:537px;background:var(--white)}
.projects .section-title{top:46px}
.projects .rule{left:582px;top:72px;background:var(--gold)}
.project{position:absolute;height:188px}

/* contact strip */
.contact-strip{top:2267px;height:96px;background:var(--red);color:var(--white)}
.contact-item{position:absolute;top:28px;display:flex;align-items:center;gap:14px}
.contact-item small{display:block;font-family:"Raleway",Arial,sans-serif;font-weight:700;font-size:11px;text-transform:uppercase}
.contact-item strong{font-family:"Raleway",Arial,sans-serif;font-weight:800;font-size:21px;line-height:24px}
.follow{left:855px;top:38px;display:flex;align-items:center;gap:9px;font-family:"Raleway",Arial,sans-serif;font-weight:700;font-size:11px}
.follow i{display:block;width:10px;height:10px;border-radius:50%;background:var(--white)}

/* footer */
.site-footer{top:2363px;height:220px;background:var(--beige)}
.footer-brand{left:253px;top:84px;display:flex;align-items:center;gap:6px}
.footer-brand .brand-mark{width:14px;height:14px}
.footer-brand .brand-name{font-size:12px}
.footer-col{position:absolute;top:58px}
.footer-col h4{font-family:"Raleway",Arial,sans-serif;font-weight:700;font-size:12px;text-transform:uppercase;color:var(--ink);margin-bottom:16px}
.footer-col li{list-style:none;font-size:9px;color:var(--muted);line-height:22.5px}
.contact-col li{text-align:center;line-height:20px}
.hours p{font-size:8.5px;line-height:12px;color:var(--muted);width:150px;margin-bottom:10px}
.hours dl{width:156px;font-size:8.5px;line-height:16px;color:var(--muted);display:grid;grid-template-columns:1fr auto}
.hours dd{color:var(--ink);font-weight:600;text-align:right}
.bottom-bar{top:2583px;height:33px;background:var(--nav);color:#bdbdbd;font-size:8px}
.bottom-bar .copy{left:234px;top:11px}
.bottom-bar .legal{left:774px;top:11px;display:flex;gap:10px}
</style>
</head>
<body>

<header class="topbar">
  <div class="brand abs"><span class="brand-mark"></span><span class="brand-name">DORVANE METAL</span></div>
  <div class="visualizer abs">VISUALIZER</div>
  <div class="call abs">
    <svg width="22" height="22" viewBox="0 0 24 24" aria-hidden="true"><path fill="#b5281f" d="M6.6 10.8a15.1 15.1 0 0 0 6.6 6.6l2.2-2.2c.3-.3.7-.4 1-.2 1.1.4 2.3.6 3.6.6.6 0 1 .4 1 1V20c0 .6-.4 1-1 1A17 17 0 0 1 3 4c0-.6.4-1 1-1h3.5c.6 0 1 .4 1 1 0 1.3.2 2.5.6 3.6.1.3 0 .7-.2 1z"/></svg>
    <div><small>Call us now!</small><strong>555-201-0765</strong></div>
  </div>
</header>

<nav class="mainnav">
  <ul>
    <li class="active">Home</li><li>About Us</li><li>Services</li><li>Gallery</li><li>Contact Us</li>
  </ul>
  <div class="btn">Get a Quote</div>
</nav>

<section class="hero">
  <div class="hero-photo" role="img" aria-label="Photo of a large beige metal-sided post frame home with dormers, a wraparound porch and a garage door under a grey sky"></div>
  <h1 class="hero-title heading abs">Complete Post Frame<br>and Garages</h1>
  <div class="btn">Get a Quote</div>
</section>

<section class="quality">
  <h2 class="heading abs">Quality Building Components</h2>
  <div class="btn">Contact Us</div>
</section>

<section class="services">
  <h2 class="section-title heading abs">Services</h2>
  <span class="rule"></span>
  <article class="card" style="left:234px">
    <div class="card-photo" role="img" aria-label="Photo of a long grey post frame building under a blue sky" style="background:linear-gradient(180deg,#4f86c8 0%,#8fb3d9 45%,#8a8f94 62%,#b39a78 100%)"></div>
    <h3>Complete Post<br>Frame Building Packages</h3>
    <p>Call us for a quote, or stop in and we can help you design</p>
  </article>
  <article class="card" style="left:485px">
    <div class="card-photo" role="img" aria-label="Photo of a red house with a grey metal roof among trees" style="background:linear-gradient(180deg,#b7c4cf 0%,#6f7c6a 40%,#8b3a2e 68%,#5c7a3e 100%)"></div>
    <h3>Residential<br>Metal Roofing</h3>
    <p>Super rib, snap-loc and a variety of metal roofing options</p>
  </article>
  <article class="card" style="left:736px">
    <div class="card-photo" role="img" aria-label="Photo of a cream gambrel barn with a maroon metal roof" style="background:linear-gradient(180deg,#b6c9da 0%,#7a3b3b 35%,#e3d6bf 62%,#8f8a72 100%)"></div>
    <h3>Commercial<br>Applications</h3>
    <p>28 gauge panels are the thickest and strongest in the industry.</p>
  </article>
  <div class="btn">All Services</div>
</section>

<section class="why">
  <div class="why-panel abs"></div>
  <div class="stats-panel abs" role="img" aria-label="Dimmed photo of a metal roofed ranch home with a long driveway"></div>
  <h2 class="heading abs" style="left:234px;top:44px;font-size:16px;color:#fff">Why Choose Us</h2>
  <span class="rule" style="left:234px"></span>
  <div class="acc-item" style="top:108px"><div class="acc-head">Construction Team<span>+</span></div></div>
  <div class="acc-item" style="top:152px"><div class="acc-head">Building Protection Services<span>+</span></div></div>
  <div class="acc-item" style="top:196px;height:117px"><div class="acc-head">Professional Plumbing<span>-</span></div>
    <p>Our crews handle every project from the first estimate to the final trim piece. We measure twice, order exact panel lengths and schedule each delivery around your site. Every building we supply is backed by trusted steel, sound fasteners and a team that answers the phone when you call.</p>
  </div>

  <h2 class="heading abs" style="left:644px;top:44px;font-size:16px;color:#fff">Statistics Company</h2>
  <span class="rule" style="left:644px"></span>
  <div class="stat" style="left:644px;top:106px"><b>10+</b><span>Years Experience</span></div>
  <div class="stat" style="left:811px;top:106px"><b>600+</b><span>Complete Projects</span></div>
  <div class="stat" style="left:644px;top:193px"><b>15+</b><span>Awards Received</span></div>
  <div class="stat" style="left:811px;top:193px"><b>600+</b><span>Complete Projects</span></div>
  <div class="btn">Get a Quote</div>
</section>

<section class="clients">
  <h2 class="heading abs">Our Client Say</h2>
  <span class="rule"></span>
  <div class="quote" style="left:234px">
    <p>The crew delivered our garage package right on time. Every panel fit cleanly and the trim matched perfectly. We would gladly order from them again for our next barn project.</p>
    <div class="author"><div class="avatar" role="img" aria-label="Client portrait"></div><div><b>Laura Benton</b><small>Designer in Studio Nine</small></div></div>
  </div>
  <div class="quote" style="left:485px">
    <p>Our new metal roof looks great and held up through a rough winter. The quote was fair and clear, and questions were answered quickly every time we called.</p>
    <div class="author"><div class="avatar" role="img" aria-label="Client portrait"></div><div><b>Marcus Hale</b><small>Developer in Studio Nine</small></div></div>
  </div>
  <div class="quote" style="left:734px">
    <p>They helped us design a shop that fits our land and our budget. Materials arrived sorted and labeled, which made the build simple for our small crew.</p>
    <div class="author"><div class="avatar" role="img" aria-label="Client portrait"></div><div><b>Nina Carver</b><small>Marketing in Studio Nine</small></div></div>
  </div>
  <div class="dots abs"><i></i><i></i><i></i></div>
</section>

<section class="projects">
  <h2 class="section-title heading abs">Amazing Projects</h2>
  <span class="rule"></span>
  <div class="project" style="left:31px;top:107px;width:276px;background:linear-gradient(180deg,#9fb6c8,#b04030 45%,#6d8a45)" role="img" aria-label="Photo of a red and grey garage with a garden in front"></div>
  <div class="project" style="left:319px;top:107px;width:274px;background:linear-gradient(180deg,#7e8a8f,#5a5d5e 35%,#8f2a25 60%,#4f7a35)" role="img" aria-label="Photo of a red barn with a dark grey roof"></div>
  <div class="project" style="left:605px;top:107px;width:276px;background:linear-gradient(180deg,#4d86cc,#a0452a 50%,#9a8a6e)" role="img" aria-label="Photo of a rust coloured garage with cupola on gravel"></div>
  <div class="project" style="left:893px;top:107px;width:276px;background:linear-gradient(180deg,#3c4450,#5d6874 40%,#c9ccd0 70%,#56663e)" role="img" aria-label="Photo of a white house with a dark metal roof"></div>
  <div class="project" style="left:31px;top:307px;width:276px;background:linear-gradient(180deg,#b9cad6,#d9d8cc 45%,#5f8746)" role="img" aria-label="Photo of a cream two storey house with a green roof"></div>
  <div class="project" style="left:319px;top:307px;width:274px;background:linear-gradient(180deg,#b9cde0,#2c2e3a 35%,#b8a78a 65%,#6f7f5a)" role="img" aria-label="Photo of a small shed with a dark roof and barn doors"></div>
  <div class="project" style="left:605px;top:307px;width:276px;background:linear-gradient(180deg,#c8d2dc,#b8bcbf 35%,#8a7a66 60%,#7a6652)" role="img" aria-label="Photo of white steel buildings beside a dirt lot"></div>
  <div class="project" style="left:893px;top:307px;width:276px;background:linear-gradient(180deg,#47535d,#2a3550 50%,#3d4234)" role="img" aria-label="Photo of a blue gambrel shed at dusk"></div>
</section>

<section class="contact-strip">
  <div class="contact-item" style="left:279px">
    <svg width="40" height="40" viewBox="0 0 40 40" aria-hidden="true"><circle cx="20" cy="20" r="18" fill="none" stroke="#fff" stroke-width="2.5"/><path fill="#fff" d="M14.5 18.5a11 11 0 0 0 7 7l2-2c.3-.3.6-.3.9-.2.9.3 1.9.5 2.9.5.5 0 .8.3.8.8v3c0 .5-.3.8-.8.8A14 14 0 0 1 11.4 12.4c0-.5.3-.8.8-.8h3c.5 0 .8.3.8.8 0 1 .2 2 .5 2.9.1.3 0 .6-.2.9z"/></svg>
    <div><small>Phone Number</small><strong>555-201-0765</strong></div>
  </div>
  <div class="contact-item" style="left:544px">
    <svg width="40" height="40" viewBox="0 0 40 40" aria-hidden="true"><rect x="11" y="5" width="18" height="9" fill="#fff"/><rect x="4" y="15" width="32" height="15" rx="3" fill="#fff"/><rect x="11" y="24" width="18" height="12" fill="#fff" stroke="#b5281f" stroke-width="2"/></svg>
    <div><small>Fax</small><strong>555-201-0994</strong></div>
  </div>
  <div class="follow abs">Follow Us: <i></i><i></i><i></i></div>
</section>

<footer class="site-footer">
  <div class="footer-brand abs"><span class="brand-mark"></span><span class="brand-name">DORVANE METAL</span></div>
  <div class="footer-col" style="left:434px">
    <h4>Useful Links</h4>
    <ul><li>Home</li><li>About Us</li><li>Services</li><li>Gallery</li><li>Contact Us</li></ul>
  </div>
  <div class="footer-col contact-col" style="left:621px">
    <h4>Contact Us</h4>
    <ul><li>Call Us: 555-201-0765</li><li>Fax: 555-201-0994</li><li>info@example.com</li></ul>
  </div>
  <div class="footer-col hours" style="left:809px">
    <h4>Working Hours</h4>
    <p>Our support available to help you 24 hours a day, seven days a week.</p>
    <dl><dt>Monday-Friday:</dt><dd>9am to 5pm</dd><dt>Saturday:</dt><dd>10am to 2pm</dd><dt>Sunday:</dt><dd>Closed</dd></dl>
  </div>
</footer>

<div class="bottom-bar" style="position:absolute;left:0;width:1200px;top:2583px;height:33px">
  <span class="copy abs">Copyright © 2019 www.dorvanemetalinc.com</span>
  <span class="legal abs"><span>Our Services</span><span>Projects</span><span>Contact Us</span><span>Privacy Policy</span></span>
</div>

</body>
</html>
```